Vaultrix Web Site

Hi Designers. Our web site at www.vaultrix.net.au needs a new look.

We do:

- off-site backup, every day, for vital data
- data recovery from crashed disks

We have an existing logo

Our colour is blue. Our image is about Trust and Competence

We are in Perth, Western Australia. Our photographs are local images.

We've been in business for fifteen years.

We have a second URL too: www.keep-our-records.com.au

Both URLs go to the same web site.

Would you like to take on this project?

Target Market(s)

Target market is small to medium business, with between 5 and 100 staff. Customers are mainly in Australia but can be anywhere. There are other providers who are cheaper- our point of difference is that we are highly professional and have been in the business for 15 years. personal attention is important to us- we promise Extreme Service.

Industry/Entity Type

Data Recovery

Requirements
Must have
• Our image is about Trust and Competence. Existing text from our web site can be used.
Should not have
• No moving Flash, no Flash intro

```html
<!DOCTYPE html>
<html lang="en">
<head>
<meta charset="utf-8">
<title>Vaultrix – Remote Backup</title>
<link rel="stylesheet" href="https://fonts.googleapis.com/css2?family=Jost:wght@400;500;600&display=swap">
<style>
  :root {
    --page-grey: #dcdcdc;
    --top-strip: #e4e4e4;
    --header-white: #f7f7f7;
    --nav-grey: #9a9a9a;
    --nav-active: #ffffff;
    --title-grey: #9c9c9c;
    --deep-blue: #004a66;
    --mid-blue: #0a6486;
    --dark-blue: #033a52;
    --panel: #ececec;
    --panel-text: #4a4a4a;
    --heading-text: #444444;
    --scroll-track: #0b4d68;
    --scroll-thumb: #125c7a;
    --caption-bg: rgba(28, 96, 130, 0.88);
    --footer: #e6e6e6;
    --footer-text: #8e8e8e;
    --logo-blue: #1d4f8c;
  }
  * { box-sizing: border-box; margin: 0; padding: 0; }
  html, body { width: 1200px; height: 781px; overflow: hidden; }
  body { font-family: "Jost", "Century Gothic", sans-serif; background: var(--page-grey); }
  .page { position: relative; width: 1200px; height: 781px; overflow: hidden; background: var(--page-grey); }

  .top-strip { position: absolute; left: 0; top: 0; width: 100%; height: 16px; background: var(--top-strip); }
  .header { position: absolute; left: 0; top: 16px; width: 100%; height: 89px;
    background: linear-gradient(90deg, #ffffff 0%, var(--header-white) 40%, #ececec 100%);
    border-radius: 0 0 0 40px; box-shadow: 0 2px 4px rgba(0,0,0,0.08); }
  .brand { position: absolute; left: 138px; top: 30px; display: flex; align-items: center; gap: 10px; }
  .brand-mark { width: 26px; height: 26px; border-radius: 50%; background: var(--logo-blue); }
  .brand-name { font-size: 26px; font-weight: 600; color: var(--logo-blue); }
  .site-title { position: absolute; left: 278px; top: 30px; font-size: 26px; font-weight: 500; color: var(--title-grey); letter-spacing: 0.3px; }
  .social { position: absolute; top: 12px; display: block; }
  .social-one { left: 1118px; width: 26px; height: 22px; border-radius: 50%; background: #c4c4c4; }
  .social-two { left: 1159px; width: 23px; height: 23px; background: #bdbdbd; }
  .search { position: absolute; left: 1027px; top: 46px; width: 157px; height: 23px; background: #d3d3d3; }
  .search svg { position: absolute; right: 7px; top: 5px; }

  .main-nav { position: absolute; right: 122px; top: 119px; display: flex; gap: 18px;
    font-size: 14px; font-weight: 500; color: var(--nav-grey); padding-bottom: 5px; border-bottom: 1px solid #c8c8c8; padding-left: 50px; }
  .main-nav .active { color: var(--nav-active); text-shadow: 0 1px 2px rgba(0,0,0,0.55); }

  .hero { position: absolute; left: 135px; top: 152px; width: 941px; height: 182px;
    background: linear-gradient(90deg, #2a2d31 0%, #7a6a5a 18%, #c88a50 30%, #2d6fa6 42%, #e9eef2 60%, #cfd8df 78%, #7f9cb4 100%); }
  .hero-caption { position: absolute; left: 633px; top: 190px; width: 443px; height: 115px;
    background: var(--caption-bg); box-shadow: 0 3px 6px rgba(0,0,0,0.35); color: #fff; padding: 11px 0 0 22px; }
  .hero-caption h2 { font-size: 21px; font-weight: 500; margin-bottom: 8px; text-shadow: 0 1px 2px rgba(0,0,0,0.4); }
  .hero-caption p { font-size: 15px; font-weight: 500; line-height: 19px; text-shadow: 0 1px 2px rgba(0,0,0,0.4); }

  .content-band { position: absolute; left: 0; top: 357px; width: 100%; height: 372px;
    background: linear-gradient(180deg, var(--deep-blue) 0%, var(--mid-blue) 35%, var(--dark-blue) 100%);
    border-top: 3px solid #0f5674; }
  .content-panel { position: absolute; left: 213px; top: 384px; width: 763px; height: 320px;
    background: var(--panel); padding: 20px 20px 0 40px; box-shadow: 0 2px 6px rgba(0,0,0,0.35); }
  .content-panel h1 { font-size: 21px; font-weight: 500; color: var(--heading-text); margin-left: 2px; margin-bottom: 7px; }
  .content-panel h3 { font-size: 17px; font-weight: 500; color: var(--heading-text); margin-left: 2px; margin-bottom: 9px; }
  .content-panel p { font-size: 11.5px; font-weight: 500; color: var(--panel-text); line-height: 18.5px; margin-bottom: 19px; }
  .scrollbar { position: absolute; left: 976px; top: 384px; width: 21px; height: 320px; background: var(--scroll-track); }
  .scroll-thumb { position: absolute; left: 3px; top: 22px; width: 15px; height: 72px; background: var(--scroll-thumb); }
  .scrollbar svg { position: absolute; left: 5px; }

  .footer { position: absolute; left: 0; top: 729px; width: 100%; height: 52px; background: var(--footer); }
  .footer-nav { position: absolute; left: 330px; top: 19px; display: flex; gap: 15px; font-size: 10.5px; font-weight: 500; color: var(--footer-text); }
  .copyright { position: absolute; right: 24px; top: 19px; font-size: 11.5px; font-weight: 500; color: var(--footer-text); }
</style>
</head>
<body>
<div class="page">
  <div class="top-strip"></div>
  <header class="header">
    <div class="brand"><span class="brand-mark"></span><span class="brand-name">Vaultrix</span></div>
    <div class="site-title">Keep our records</div>
    <span class="social social-one" aria-label="Social link"></span>
    <span class="social social-two" aria-label="Social link"></span>
    <div class="search">
      <svg width="12" height="12" viewBox="0 0 12 12" aria-hidden="true">
        <circle cx="5" cy="5" r="3.6" fill="none" stroke="#fff" stroke-width="1.8"/>
        <line x1="7.6" y1="7.6" x2="11" y2="11" stroke="#fff" stroke-width="2"/>
      </svg>
    </div>
  </header>

  <nav class="main-nav">
    <span>Home</span><span>About Us</span><span class="active">Remote Backup</span><span>Emergency Recovery</span><span>Testimonials</span><span>Our Clients</span><span>Contact Us</span>
  </nav>

  <div class="hero" role="img" aria-label="Photograph of a smiling woman in a blue sweater at a bright office desk"></div>
  <div class="hero-caption">
    <h2>Off- site Backup</h2>
    <p>We store an encrypted backup of your data files at<br>a remote location, in Perth, Western Australia,<br>the safest place in the world for your critical information</p>
  </div>

  <div class="content-band"></div>
  <main class="content-panel">
    <h1>REMOTE BACKUP - Off Site, Every Night</h1>
    <h3>Here’s how it works...</h3>
    <p>Vaultrix Computer Services operates secure Backup Servers at our WestLink Data Centre.<br>Your system runs a program called a Backup Client on your File Server.</p>
    <p>Your File Server remains on at night. While your business is closed the software checks to see which files have been used<br>that day, and which need to be backed up.</p>
    <p>The software makes an encrypted and compressed set of backup files. It then connects automatically with the Backup Server<br>by one of the available methods and sends the backup. Our Server stores the data and the client computer disconnects.</p>
    <p>Forget about trying to keep track of external drives, tapes and DVDs. With Vaultrix, you know your data is secure,<br>and you don't have to remember to backup! Vaultrix does it for you.</p>
  </main>
  <div class="scrollbar">
    <svg style="top:6px" width="11" height="7" viewBox="0 0 11 7" aria-hidden="true"><polyline points="1,6 5.5,1.5 10,6" fill="none" stroke="#3f86a6" stroke-width="1.6"/></svg>
    <div class="scroll-thumb"></div>
    <svg style="bottom:6px" width="11" height="7" viewBox="0 0 11 7" aria-hidden="true"><polyline points="1,1 5.5,5.5 10,1" fill="none" stroke="#3f86a6" stroke-width="1.6"/></svg>
  </div>

  <footer class="footer">
    <nav class="footer-nav">
      <span>Home</span><span>About Us</span><span>Remote Backup</span><span>Emergency Recovery</span><span>Testimonials</span><span>Our Clients</span><span>Contact Us</span>
    </nav>
    <div class="copyright">© 2011 - Vaultrix Computer Services</div>
  </footer>
</div>
</body>
</html>
```